Criação de Papelaria (6 itens) para Brisa & Coral
" Serviços Exclusivos p/ Receptivo Turistico. Aluguel de Carros e Motos - Roteiros - Transfers - Reservas e Enxovais "

```html
<!DOCTYPE html>
<html lang="pt-BR">
<head>
<meta charset="UTF-8">
<title>Brisa &amp; Coral – Papel Timbrado</title>
<link href="https://fonts.googleapis.com/css2?family=Open+Sans:ital,wght@0,400;0,600;1,400&display=swap" rel="stylesheet">
<style>
  :root {
    --backdrop: #ebe9e5;
    --paper: #ffffff;
    --gold: #b8893e;
    --gold-light: #e6c58a;
    --gold-dark: #9a6e2c;
    --ink: #2b2b2b;
    --rule: #1e1e1e;
    --mark: #ececec;
  }
  * { margin: 0; padding: 0; box-sizing: border-box; }
  html, body { width: 1200px; height: 1200px; overflow: hidden; }
  body {
    background: var(--backdrop);
    display: flex;
    align-items: center;
    justify-content: center;
    font-family: "Open Sans", Arial, sans-serif;
  }
  .letterhead {
    position: relative;
    width: 778px;
    height: 1100px;
    background: var(--paper);
    box-shadow: 0 2px 12px rgba(0,0,0,0.08);
    overflow: hidden;
  }
  .brand {
    position: absolute;
    top: 70px;
    right: 70px;
    font-weight: 600;
    font-size: 34px;
    color: var(--gold);
    letter-spacing: 0.5px;
  }
  .brand-tagline {
    display: block;
    font-size: 34px;
  }
  .center-mark {
    position: absolute;
    left: 50%;
    top: 430px;
    width: 230px;
    height: 230px;
    margin-left: -115px;
    border-radius: 50%;
    background: var(--mark);
  }
  .footer {
    position: absolute;
    left: 70px;
    right: 70px;
    bottom: 70px;
  }
  .footer-rule {
    height: 2px;
    background: var(--rule);
  }
  .contact {
    list-style: none;
    margin: 10px 0 0;
    font-style: italic;
    font-size: 13px;
    line-height: 1.55;
    color: var(--ink);
  }
  .website {
    margin: 34px 0 8px;
    text-align: right;
    font-style: italic;
    font-size: 13px;
    color: var(--ink);
  }
  .website-label { margin-right: 36px; }
  .gold-edge {
    position: absolute;
    left: 0;
    right: 0;
    bottom: 0;
    height: 16px;
    background: linear-gradient(90deg, var(--gold-light), var(--gold) 45%, var(--gold-light) 75%, var(--gold-dark));
  }
</style>
</head>
<body>
  <main class="letterhead">
    <header class="brand">Brisa &amp; Coral</header>

    <div class="center-mark" aria-hidden="true"></div>

    <footer class="footer">
      <div class="footer-rule"></div>
      <ul class="contact">
        <li>Phone: (13) 3456-7890</li>
        <li>Rua das Gaivotas, 420</li>
        <li>Sala 12 - Santos - 11015-300</li>
      </ul>
      <p class="website"><span class="website-label">Website</span>www.brisaecoral.com.br</p>
      <div class="footer-rule"></div>
    </footer>

    <div class="gold-edge"></div>
  </main>
</body>
</html>
```